Plastic Surgeon Stationary Design

I Already have the logo. I Want and a clean, minimalist and elegant project. Please, I prefer Black, White and Gold color but you're free to try another ones. Business card,
Letterhead (A4 and Office), Recipes (Letter Pad) (A5), Envelop, Invoice, Computer Bill, Bill Book, Single A4 page size,
You Have to create at least the same materials I already own. I would like to a file to use in word to print letterheads and letter pad.
What I want that you make more changes are the envelopes that are to colorful and not elegant.
I'll not accept any design without my addresses as you can guide yourself with the models I provide.
Here are the addresses too:
"www.clevandrotavares.example" (website)
(My clinics' address)
"SÃO PAULO
Rua Heitor Lunardi, 1870, Lunardi Corporate, Cj 204
São Paulo - SP
(11) 98432-6120"
"BALNEÁRIO CAMBORIÚ
Rua Benedito Kauer, 418, 7° andar
Edificio Vale Azul
Balneário Camboriú - SC
(047) 9246-3180"
Attention: Letterheads, Recipes, have to contain "CRM/SC 27.583 and CRM/SP 238.416" close to my name (Dr. Clevandro Tavares - Cirurgião Plástico), it is usually placed at the bottom.
Designers, attention!
During the process of creating bear in mind that the details of the logo, as the faces on the sides, are designed to be subtle. Highlight other such details affect the delicacy and elegance of the logo and visual identity.
When you are creating stationery, do not abuse the use of the logo, it should be used once or at most two times in each item.
Remember! Each stationery set must submit 3 models, one with the address "Balneario Camboriu", another with the address of "São Paulo" and the third containing both addresses.
The model letter envelope, folder type bag for letterhead and folder with inner pocket that provided a model did not please me because they are very flashy. Give preference to the use of white or black background.
PLEASE! Seek inspiration in the models contained in this link:
https://www.filecrate.example/sh/kq27pz58wnr4c1v/MbTyLo_QaZ
In this link you can find my PAST Stationary Itens, so it can help you on your work
https://stashbin.example/8RkLQ2vNm3TeHwYz
Reason: Nobody presented anything useful.
Reason: still waiting some designers send their projects
Reason: Still Waiting Some Designs....
Target Market(s)
Mostly females with good economical condition. (Class A and AB)
Industry/Entity Type
Business
Requirements
Must have
- You have to provide 3 models of each paper, one with the address of São Paulo, another with the Balneario Camboriú address, and the third one with both addresses.

```html
<!DOCTYPE html>
<html lang="pt-BR">
<head>
<meta charset="utf-8">
<title>Clevandro Tavares – Stationery Set</title>
<link href="https://fonts.googleapis.com/css2?family=Open+Sans:ital,wght@0,400;0,600;0,700;1,400&display=swap" rel="stylesheet">
<style>
  :root{
    --bg:#ededed;
    --paper:#f7f7f7;
    --paper-edge:#e2e2e2;
    --ink:#1b1b1b;
    --text:#3a3a3a;
    --muted:#6b6b6b;
    --accent:#d8793f;
    --faint:#e4e4e4;
  }
  *{box-sizing:border-box;margin:0;padding:0}
  html,body{width:1200px;height:1000px;overflow:hidden}
  body{background:var(--bg);font-family:"Open Sans",Arial,sans-serif;color:var(--text);position:relative}
  .sheet{position:absolute;background:var(--paper);border:1px solid var(--paper-edge);overflow:hidden}
  .brand{display:flex;align-items:center;gap:6px;color:var(--ink);font-weight:700;white-space:nowrap;letter-spacing:-.01em}
  .brand-dot{border-radius:50%;background:var(--ink);flex:none}
  .ico{display:inline-block;width:4px;height:4px;border-radius:50%;background:var(--accent);margin-right:2px;vertical-align:middle}
  .label{text-transform:uppercase}

  /* Letterhead */
  .letterhead{left:212px;top:125px;width:376px;height:523px}
  .letterhead .brand{position:absolute;left:0;right:0;top:48px;justify-content:center;font-size:16px}
  .letterhead .brand-dot{width:13px;height:13px}
  .letter-watermark{position:absolute;left:98px;top:330px;width:122px;height:122px;border-radius:50%;background:var(--faint)}
  .letter-body{position:absolute;left:60px;top:137px;width:255px;font-size:5.6px;line-height:8.6px;text-align:justify;color:var(--text)}
  .letter-body p{margin-bottom:8.6px}
  .signature{position:absolute;left:178px;top:365px;width:135px;height:28px;background:#e9e9e9;border-radius:2px}
  .letter-footer{position:absolute;top:470px;font-size:4.6px;line-height:6.2px;color:var(--muted);white-space:nowrap}
  .footer-bc{left:18px}
  .footer-crm{left:130px;width:116px;text-align:center;top:480px}
  .footer-sp{left:286px}

  /* Folder */
  .folder-pages{left:645px;top:100px;width:435px;height:548px}
  .folder-pages::before,.folder-pages::after{content:"";position:absolute;top:-1px;bottom:-1px;width:1px;background:var(--paper-edge)}
  .folder-pages::before{left:4px}
  .folder-pages::after{left:8px}
  .folder{left:657px;top:100px;width:423px;height:548px}
  .folder .brand{position:absolute;left:74px;top:148px;font-size:25px;gap:10px}
  .folder .brand-dot{width:20px;height:20px}

  /* Business cards */
  .card{width:155px;height:94px}
  .card-front{left:81px;top:692px}
  .card-front .brand{position:absolute;left:0;right:0;top:40px;justify-content:center;font-size:9px;gap:4px}
  .card-front .brand-dot{width:8px;height:8px}
  .card-back{left:81px;top:812px;text-align:center}
  .card-back .mark{width:8px;height:8px;border-radius:50%;background:var(--ink);margin:9px auto 3px}
  .card-back .name{font-size:7px;font-weight:700;color:var(--ink);line-height:9px}
  .card-back .role{font-size:4.4px;font-style:italic;line-height:5.8px}
  .card-back .contacts{position:absolute;left:8px;right:8px;bottom:9px;display:flex;justify-content:space-between;align-items:flex-start;text-align:left;font-size:3px;line-height:4.2px;color:var(--muted);white-space:nowrap}
  .card-back .contacts .ico{width:3px;height:3px;margin-right:1px}

  /* Envelopes */
  .envelope{top:707px;width:412px;height:196px}
  .envelope-front{left:290px}
  .envelope-front .brand{position:absolute;left:22px;top:145px;font-size:12px;gap:5px}
  .envelope-front .brand-dot{width:10px;height:10px}
  .envelope-back{left:742px}
  .envelope-back svg{position:absolute;inset:0}
  .envelope-back .brand{position:absolute;left:308px;top:47px;font-size:7.5px;gap:3px}
  .envelope-back .brand-dot{width:6px;height:6px}
  .envelope-back .address{position:absolute;left:308px;top:70px;font-size:4.6px;line-height:6px;color:var(--muted);white-space:nowrap}
  .envelope-back .address p{margin-bottom:5px}
</style>
</head>
<body>

<section class="sheet letterhead" aria-label="Letterhead">
  <div class="brand"><span class="brand-dot"></span>Clevandro Tavares</div>
  <div class="letter-watermark" aria-hidden="true"></div>
  <div class="letter-body">
    <p>Dear Client</p>
    <p>Lorem ipsum dolor sit amet, consectetur adipiscing elit. Nulla sodales nisi vitae Lorem ipsum dolor sit amet, consectetur adipiscing elit. Suspendisse feugiat eros nisl, a facilisis risus eleifend sed. Aliquam mauris enim, fermentum eu lacinia sit amet, laoreet eu leo. Nullam eleifend nulla in libero tristique, ac vulputate odio tincidunt. Etiam non condimentum tortor. Integer suscipit neque nec odio porttitor cursus. Phasellus a sapien blandit, suscipit justo id, condimentum ante. Morbi tristique justo risus, id mattis dui molestie ut. Nullam volutpat ut quam commodo faucibus. Pellentesque urna est, interdum in elit quis, pharetra elementum orci. Nam pharetra velit molestie justo placerat scelerisque.</p>
    <p>ullam aliquam ligula ac sem aliquet varius. Nullam sed laoreet sapien. Fusce ultricies lobortis odio, sed imperdiet magna lacinia egestas. Morbi vitae varius nibh. Phasellus purus felis, congue id semper quis, porttitor ut sem. Integer turpis nunc, posuere at quam interdum, interdum pharetra lectus. Fusce commodo sapien vel consequat tincidunt. Proin sed nisl dignissim, accumsan dui ut, luctus turpis. Praesent vulputate elementum nibh. Ut volutpat felis ut mi tincidunt, vitae accumsan quam porta. Sed malesuada bibendum lectus tempor ullamcorper. Nullam interdum diam velit, id porta elit congue quis.</p>
    <p>Best regards,</p>
  </div>
  <div class="signature" role="img" aria-label="Handwritten signature of Dr. Clevandro Tavares"></div>
  <div class="letter-footer footer-bc">
    <span class="label">Balneário Camboriú</span><br>
    <span class="ico"></span>Rua Benedito Kauer, 418,<br>
    7° andar Edificio Vale Azul<br>
    Balneário Camboriú - SC<br>
    <span class="ico"></span>(047) 9246-3180
  </div>
  <div class="letter-footer footer-crm">
    CRM/SC 27.583<br>CRM/SP 238.416<br><br>
    <span class="ico"></span>www.clevandrotavares.example
  </div>
  <div class="letter-footer footer-sp">
    <span class="label">São Paulo</span><br>
    <span class="ico"></span>Rua Heitor Lunardi, 1870,<br>
    Lunardi Corporate, Cj 204<br>
    São Paulo - SP<br>
    <span class="ico"></span>(11) 98432-6120
  </div>
</section>

<div class="sheet folder-pages" aria-hidden="true"></div>
<section class="sheet folder" aria-label="Presentation folder">
  <div class="brand"><span class="brand-dot"></span>Clevandro Tavares</div>
</section>

<section class="sheet card card-front" aria-label="Business card front">
  <div class="brand"><span class="brand-dot"></span>Clevandro Tavares</div>
</section>

<section class="sheet card card-back" aria-label="Business card back">
  <div class="mark"></div>
  <div class="name">Dr. Clevandro Tavares</div>
  <div class="role">Cirurgião Plástico<br>Membro da Associação Nacional de Cirurgia Estética<br>CRM/SC 27.583 · CRM/SP 238.416</div>
  <div class="contacts">
    <div>BALNEÁRIO CAMBORIÚ<br>Rua Benedito Kauer, 418,<br>7° andar Edificio Vale Azul<br>(047) 9246-3180</div>
    <div><span class="ico"></span>www.clevandrotavares.example</div>
    <div>SÃO PAULO<br>Rua Heitor Lunardi, 1870,<br>Lunardi Corporate, Cj 204<br>(11) 98432-6120</div>
  </div>
</section>

<section class="sheet envelope envelope-front" aria-label="Envelope front">
  <div class="brand"><span class="brand-dot"></span>Clevandro Tavares</div>
</section>

<section class="sheet envelope envelope-back" aria-label="Envelope back">
  <svg width="412" height="196" viewBox="0 0 412 196" aria-hidden="true">
    <polyline points="2,4 48,68 364,68 410,4" fill="none" stroke="#dcdcdc" stroke-width="1"/>
  </svg>
  <div class="brand"><span class="brand-dot"></span>Clevandro Tavares</div>
  <div class="address">
    <p>SÃO PAULO<br><span class="ico"></span>Rua Heitor Lunardi, 1870,<br>Lunardi Corporate, Cj 204<br>São Paulo - SP<br><span class="ico"></span>(11) 98432-6120</p>
    <p>BALNEÁRIO CAMBORIÚ<br><span class="ico"></span>Rua Benedito Kauer, 418,<br>7° andar Edificio Vale Azul<br>Balneário Camboriú - SC<br><span class="ico"></span>(047) 9246-3180</p>
    <p><span class="ico"></span>www.clevandrotavares.example</p>
  </div>
</section>

</body>
</html>
```